3 -fold flyer about Mara's Greenfields

I need a flyer for Mara's Greenfields. It will tell folks more about my dressings and dipping sauce and the importance of organic food. It will tell folks the history of how I came to bottle the dressings and where they are currently available. and that I plan to expand.

Best compliments I've received are: "I would eat that stuff (Golden Harvest Dunking Sauce" on DOG FOOD!"
and
"I don't have friends over any more for dinner because they always eat all my Mara's Greenfields dressings!"

Most of the info is already on my website at marasgreenfields.example
I am really busy getting ready for a festival July 16-20, so won't be available at all those dates. I will be minimally available before then. Will be back 'online' on Tuesday, the 21st.

Hope to hear from you soon ! thanks!

```html
<!DOCTYPE html>
<html lang="en">
<head>
<meta charset="utf-8">
<title>Mara's Greenfields – Tri-fold Flyer</title>
<link href="https://fonts.googleapis.com/css2?family=Open+Sans:ital,wght@0,400;0,600;0,700;0,800;1,400;1,700&family=PT+Sans+Narrow:wght@400;700&display=swap" rel="stylesheet">
<style>
  :root{
    --stage:#9b3f8d;
    --purple:#7a1f6e;
    --purple-deep:#5e1656;
    --yellow:#f3ec1e;
    --amber:#f2b318;
    --orange:#f4a21a;
    --green:#7cc242;
    --green-dark:#5d8a2c;
    --ink:#2a1a10;
    --white:#ffffff;
  }
  *{box-sizing:border-box;margin:0;padding:0}
  html,body{width:846px;height:1200px;overflow:hidden}
  body{background:var(--stage);font-family:"Open Sans",Arial,sans-serif;color:var(--ink);position:relative}
  .sheet{position:absolute;display:flex;box-shadow:0 6px 18px rgba(40,0,40,.35)}
  .sheet--outside{left:90px;top:52px;width:685px;height:532px}
  .sheet--inside{left:86px;top:600px;width:684px;height:536px}
  .panel{position:relative;width:228px;height:100%;overflow:hidden}
  .panel + .panel{border-left:1px solid rgba(120,100,0,.25)}
  .meadow{background:linear-gradient(180deg,var(--yellow) 0%,#e6e41f 40%,#b5d637 75%,var(--green) 100%)}
  .meadow--warm{background:linear-gradient(180deg,#eee61c 0%,var(--orange) 55%,#b8cf34 82%,var(--green) 100%)}
  .scenery{position:absolute;left:0;right:0;bottom:0;height:45%;
    background:linear-gradient(180deg,rgba(93,138,44,0) 0%,rgba(93,138,44,.45) 100%)}
  .brand{font-family:"Open Sans",Arial,sans-serif;font-weight:800;color:var(--purple);text-align:center;line-height:1;white-space:nowrap}
  .claims{font-family:"PT Sans Narrow",Arial,sans-serif;font-weight:700;color:var(--purple);text-align:center;letter-spacing:.3px;white-space:nowrap}
  /* outside: story panel */
  .story{position:absolute;left:30px;top:108px;width:182px;height:324px;background:var(--amber);
    border:2px solid #d9930f;border-radius:40px 40px 30px 30px;padding:26px 13px 12px;font-size:9.6px;line-height:1.32;text-align:justify}
  .story strong{font-weight:700}
  .expanding{position:absolute;left:26px;top:484px;font-family:"PT Sans Narrow",Arial,sans-serif;font-weight:700;font-size:25px;color:var(--purple);letter-spacing:-.3px;white-space:nowrap}
  /* outside: contact panel */
  .contact{position:absolute;left:22px;top:158px;width:200px}
  .contact h3{font-family:"PT Sans Narrow",Arial,sans-serif;font-size:15px;color:var(--purple);margin-left:26px}
  .contact p{font-size:9.2px;line-height:1.45;margin-left:26px;white-space:nowrap}
  .contact .icon{position:absolute;left:0}
  .caller{position:absolute;left:26px;top:376px;width:180px;height:58px;background:linear-gradient(180deg,var(--purple) 0%,var(--purple-deep) 100%);
    border-radius:16px;color:var(--white);text-align:center;padding-top:14px}
  .caller b{display:block;font-size:15px;font-weight:700;line-height:1.2}
  .caller i{font-size:11px;font-weight:700}
  .caller .icon{position:absolute;left:85px;top:3px}
  .web{position:absolute;left:0;right:0;top:490px;text-align:center;font-size:9.4px;font-weight:700;letter-spacing:1px;color:var(--purple);white-space:nowrap}
  .badges{position:absolute;left:88px;top:440px;display:flex;gap:18px}
  .badge{width:36px;height:36px;background:var(--white);border:2px solid var(--green-dark)}
  .badge--round{border-radius:50%}
  /* inside */
  .welcome{background:var(--purple)}
  .welcome-top{height:154px;background:var(--white);display:flex;align-items:center;justify-content:center}
  .reviews{color:var(--white);padding:26px 14px 0 18px}
  .reviews h4{font-style:italic;font-weight:400;font-size:17px;margin:0 0 24px 28px;font-family:"PT Sans Narrow",Arial,sans-serif}
  .reviews blockquote{font-weight:700;font-size:15.5px;line-height:1.3;margin-bottom:20px}
  .menu{padding:12px 10px 0 14px}
  .menu h2,.find h2{font-family:"PT Sans Narrow",Arial,sans-serif;font-weight:700;font-size:20px;color:var(--purple);line-height:1;white-space:nowrap}
  .menu .intro{font-size:7.9px;font-weight:700;line-height:1.3;margin:5px 0 6px;text-align:justify}
  .product{display:grid;grid-template-columns:100px 1fr;column-gap:6px;margin-bottom:6px}
  .label{height:58px;border:1px solid rgba(0,0,0,.25)}
  .label--green{background:linear-gradient(180deg,#2aa85a,#0f7a3c)}
  .label--amber{background:linear-gradient(180deg,#f7c23a,#e88c14)}
  .product h5{font-family:"PT Sans Narrow",Arial,sans-serif;font-weight:700;font-size:13px;color:var(--purple);line-height:1.05}
  .product em{display:block;font-size:7.6px;line-height:1.35;margin-top:3px}
  .product .uses{grid-column:1 / 3;font-size:8px;font-weight:700;line-height:1.3;margin-top:4px}
  .find{padding:30px 14px 0 16px}
  .find p{position:relative;font-weight:700;font-size:12.6px;line-height:1.45;margin-top:10px;overflow-wrap:anywhere}
  .find .email{position:absolute;left:0;right:0;top:356px;text-align:center;font-weight:700;font-size:12.6px;line-height:1.3;padding:0 14px;overflow-wrap:anywhere}
</style>
</head>
<body>

<!-- Outside spread -->
<section class="sheet sheet--outside">
  <article class="panel meadow">
    <div class="scenery" role="img" aria-label="Illustrated redwood forest and hillside scenery in green tones"></div>
    <div class="story">
      <strong>Mara's Greenfields</strong> began as a vegan catering business in Humboldt County, California. A small but very vocal group of passionate customers encouraged Mara to bottle her savory dressings and sauces, and now you too can enjoy her dressings without the wait.<br>
      <strong>Our high-quality organic dressings and sauces are created with the belief that a healthy balanced diet maintains a synergy between great taste and ingredients that are sustainably raised and harvested.</strong>
      We only offer high life vibrancy ingredients with a variety of colors, flavors, and textures to transform simple foods into the extraordinary. Enjoy!
    </div>
    <div class="expanding">WE ARE EXPANDING</div>
  </article>

  <article class="panel meadow--warm">
    <div class="scenery" role="img" aria-label="Illustrated pine trees and hills in green tones"></div>
    <div class="brand" style="position:absolute;left:0;right:0;top:78px;font-size:19px">Mara's Greenfields</div>
    <div class="claims" style="position:absolute;left:0;right:0;top:132px;font-size:11px">DELICIOUS · GLUTEN-FREE · VEGAN</div>
    <div class="contact">
      <svg class="icon" style="top:16px" width="22" height="20" viewBox="0 0 22 20" aria-hidden="true"><path d="M11 1 L21 10 H18 V19 H4 V10 H1 Z" fill="var(--green-dark)"/></svg>
      <svg class="icon" style="top:47px" width="18" height="12" viewBox="0 0 18 12" aria-hidden="true"><rect x="1" y="1" width="16" height="10" fill="none" stroke="var(--green-dark)" stroke-width="1.5"/><path d="M1 1 L9 7 L17 1" fill="none" stroke="var(--green-dark)" stroke-width="1.5"/></svg>
      <h3>Mara's Greenfields</h3>
      <p>CATERING, DRESSING &amp; SAUCES<br>PO BOX 412, FERNVALE, CA 90000<br>info@marasgreenfields.example</p>
    </div>
    <div class="caller">
      <svg class="icon" width="10" height="10" viewBox="0 0 10 10" aria-hidden="true"><path d="M2 1 Q0 5 5 9 L7 7 L5 5 L4 6 Q2 4 3 3 L4 2 Z" fill="var(--white)"/></svg>
      <b>Mara Ellison</b><i>Sauce Boss (555) 014-2273</i>
    </div>
    <div class="web">www.marasgreenfields.example</div>
  </article>

  <article class="panel meadow">
    <div class="scenery" role="img" aria-label="Illustrated forest edge and rolling hills in green tones"></div>
    <div class="brand" style="position:absolute;left:0;right:0;top:262px;font-size:20px">Mara's Greenfields</div>
    <div class="claims" style="position:absolute;left:0;right:0;top:312px;font-size:12px">DELICIOUS · GLUTEN-FREE · VEGAN</div>
    <div class="badges"><div class="badge"></div><div class="badge badge--round"></div></div>
  </article>
</section>

<!-- Inside spread -->
<section class="sheet sheet--inside">
  <article class="panel welcome">
    <div class="welcome-top"><div class="brand" style="font-size:20px">Mara's Greenfields</div></div>
    <div class="reviews">
      <h4>Just a couple reviews</h4>
      <blockquote>“I would eat that stuff (Golden Harvest Dunking Sauce) on DOG FOOD!”</blockquote>
      <blockquote>“I don't have friends over any more for dinner because they always eat all my Mara's Greenfields dressings!”</blockquote>
    </div>
  </article>

  <article class="panel meadow menu">
    <h2>DRESSINGS &amp; SAUCES</h2>
    <p class="intro">We believe the key to any diet is having a wide variety of meals that satisfy your “taste” as well as provide the nutrition that you need. Our organic, gluten-free, vegan dressings and sauces offer delicious ways to maintain a healthy, tasty, vegan-based diet with high nutritional content and life vibration. The possibilities abound.</p>
    <div class="product">
      <div class="label label--green" role="img" aria-label="Golden Harvest Dunking Sauce bottle label"></div>
      <div><h5>Golden Harvest Dunking Sauce</h5><em>Oh My. Makes everything you dip in to it taste great!</em></div>
      <div class="uses">Delicious on Sandwiches, Steamed Veggies, Pasta and just about everything else!</div>
    </div>
    <div class="product">
      <div class="label label--amber" role="img" aria-label="Tahini Dressing bottle label"></div>
      <div><h5>Tahini Dressing</h5><em>The first one folks fell in love with! Just the right amount of zest.</em></div>
      <div class="uses">Delicious on Salads, Rice, Potatoes and Raw Veggies.</div>
    </div>
    <div class="product">
      <div class="label label--amber" role="img" aria-label="Curry Dressing bottle label"></div>
      <div><h5>Curry Dressing</h5><em>All we can say is: Thank Goodness for the spice trade!</em></div>
      <div class="uses">Delicious on Noodles, Rice, Tofu, Stir-Fried Veggies and Salad.</div>
    </div>
    <div class="product">
      <div class="label label--amber" role="img" aria-label="Ginger Miso Dressing bottle label"></div>
      <div><h5>Ginger Miso Dressing</h5><em>Creamy and yummy, with just enough zing!</em></div>
      <div class="uses">Delicious on Tempeh, Tofu, Rice, Pasta, Veggies, Fish and Salads.</div>
    </div>
  </article>

  <article class="panel meadow--warm find">
    <div class="scenery" role="img" aria-label="Illustrated redwood branches and hillside in green tones"></div>
    <h2 style="font-size:22px;position:relative">WHERE TO FIND US</h2>
    <p>Mara's Greenfields is currently manufactured and available only in Humboldt County, California. It is our desire to grow to be available up and down the West Coast. If you would like to see it in a store near you, please send the name and address of the store by emailing us at info@<wbr>marasgreenfields.example</p>
    <div class="email">Email us at<br>info@<wbr>marasgreenfields.example<br>to find where you can find us today</div>
  </article>
</section>

</body>
</html>
```